recipe card template

desgin an AI file that is a template for a recipe card. We are an Organic beef farm wanting to give customers recipe cards for our different beef cuts. Looking at doing something black & white that says premium product from a family farm.

Target Market(s)

people who want quality produce

Industry/Entity Type

Farm

Font styles to use
Serif
Sans Serif

Colors

Designer to choose colors to be used in the design.

Requirements
Must have
• Instruction section - ingredients section - "stonebrook larder family farm" title
Nice to have
• images etc that refer to beef and eggs

```html
<!DOCTYPE html>
<html lang="en">
<head>
<meta charset="utf-8">
<title>Stonebrook Larder Family Farm – Chuck Recipe Card</title>
<link href="https://fonts.googleapis.com/css2?family=Lato:wght@300;400;700&family=Oswald:wght@300;400&family=Pacifico&display=swap" rel="stylesheet">
<style>
  :root {
    --page-bg: #e6e2da;
    --card-bg: #f3f3f3;
    --sage: #8fae7f;
    --sage-dark: #6f8f62;
    --sage-light: #a9c596;
    --ink: #5a5a5a;
    --icon-grey: #8a8a8a;
    --photo-dark: #1d1a18;
    --photo-mid: #4a2e22;
    --photo-warm: #7a4a33;
    --cream: #f4efe6;
  }
  * { box-sizing: border-box; margin: 0; padding: 0; }
  html, body { width: 1104px; height: 1200px; overflow: hidden; }
  body {
    background: var(--page-bg);
    font-family: "Lato", sans-serif;
    position: relative;
  }
  .recipe-card {
    position: absolute;
    left: 52px; top: 255px;
    width: 1000px; height: 690px;
    display: flex;
    background: var(--card-bg);
    box-shadow: 0 6px 18px rgba(0,0,0,0.18);
  }
  .feature-panel {
    position: relative;
    width: 340px; height: 100%;
    color: var(--cream);
    overflow: hidden;
  }
  .feature-photo {
    position: absolute; inset: 0;
    background:
      radial-gradient(ellipse at 55% 38%, var(--photo-warm) 0%, var(--photo-mid) 35%, transparent 65%),
      linear-gradient(180deg, #2a211c 0%, var(--photo-mid) 45%, var(--photo-dark) 100%);
  }
  .farm-mark {
    position: absolute;
    left: 0; right: 0; top: 420px;
    display: flex; align-items: center; justify-content: center; gap: 8px;
    font-family: "Lato", sans-serif; font-weight: 400;
    font-size: 17px; letter-spacing: 1px; color: var(--cream);
  }
  .farm-mark .mark-dot {
    width: 10px; height: 10px; border-radius: 50%;
    background: var(--cream);
  }
  .feature-text {
    position: absolute;
    left: 20px; right: 20px; top: 510px;
    border-top: 2px solid var(--sage);
    padding-top: 14px;
    text-align: center;
  }
  .farm-name {
    font-family: "Lato", sans-serif; font-weight: 400;
    font-size: 27px; line-height: 34px;
    text-transform: uppercase; color: var(--sage-light);
  }
  .recipe-meta {
    margin-top: 10px;
    font-size: 16px; line-height: 23px; color: #ffffff;
  }
  .recipe-meta .label { text-transform: uppercase; }
  .recipe-panel { position: relative; flex: 1; }
  .title-band {
    position: absolute; left: 0; right: 0; top: 22px; height: 64px;
    background: var(--sage);
  }
  .recipe-title {
    position: absolute; left: 20px; top: -2px;
    font-family: "Pacifico", cursive; font-weight: 400;
    font-size: 40px; color: #ffffff; line-height: 64px;
  }
  .recipe-section { position: absolute; left: 28px; }
  .recipe-section.ingredients { top: 110px; }
  .recipe-section.instructions { top: 245px; left: 24px; }
  .section-heading {
    font-family: "Oswald", sans-serif; font-weight: 300;
    font-size: 27px; color: var(--sage-dark); text-transform: uppercase;
    line-height: 36px;
  }
  .instructions .section-heading { color: var(--sage-light); }
  .section-body { font-size: 18px; color: var(--ink); font-weight: 400; }
  .cuts-diagram {
    position: absolute; left: 0; top: 455px;
    width: 360px; height: 220px;
    background:
      radial-gradient(ellipse at 62% 35%, var(--sage) 0%, var(--sage) 14%, transparent 26%),
      linear-gradient(180deg, #a8a8a8 0%, #9a9a9a 100%);
    border-radius: 40px 70px 20px 20px;
    opacity: 0.9;
  }
  .social {
    position: absolute; left: 405px; top: 615px;
    color: var(--icon-grey);
  }
  .social-label { font-size: 18px; font-weight: 300; }
  .social-icons { display: flex; gap: 12px; margin-top: 8px; }
  .social-icons span {
    width: 20px; height: 20px; border-radius: 3px;
    background: var(--icon-grey);
  }
</style>
</head>
<body>
  <article class="recipe-card">
    <section class="feature-panel">
      <div class="feature-photo" role="img" aria-label="Photo of a grilled chuck steak with tomatoes, garlic, grilled zucchini and thyme on a dark board"></div>
      <div class="farm-mark"><span class="mark-dot"></span>HOLLOW OAK FARMS</div>
      <div class="feature-text">
        <h2 class="farm-name">Stonebrook Larder Family Farm</h2>
        <p class="recipe-meta"><span class="label">Total time:</span> 45 minutes<br><span class="label">Servings:</span> 2</p>
      </div>
    </section>
    <section class="recipe-panel">
      <div class="title-band"><h1 class="recipe-title">Chuck Recipe</h1></div>
      <div class="recipe-section ingredients">
        <h3 class="section-heading">Ingredients:</h3>
        <p class="section-body">Lorem ipasum</p>
      </div>
      <div class="recipe-section instructions">
        <h3 class="section-heading">Instruction:</h3>
        <p class="section-body">Lorem ipasum</p>
      </div>
      <div class="cuts-diagram" role="img" aria-label="Grey beef cuts diagram of a cow with the chuck section highlighted in green"></div>
      <div class="social">
        <p class="social-label">find us on:</p>
        <div class="social-icons" aria-hidden="true"><span></span><span></span><span></span><span></span><span></span></div>
      </div>
    </section>
  </article>
</body>
</html>
```